Book Cover Design Project

NOTE. I need the design in four days of posting this!

This will be the cover of my first book, WALK THE HIGH LINE -
meaning at work in modern business. The book explains defines what Purpose and Meaning is, and how to use it in business. I have included the first chapter to provide a background.

I want the core colours to be black and white, and use the colours Violet, Cerulean Blue Extra Pale (powder blue), Cadmium Lemon (flouro yellow). I plan on using this design as the basis for future books in the WALK THE HIGH LINE series, where the yellow is carried through but the violet and blue colours changing.

This is a spiritual business book without using any spiritual language. It is strongly masculine and direct in its nature.

What I am looking for is something Remarkable that captures my reader immediately. My reader is a seeker. He/she is an entrepreneur perhaps looking to setup a new venture and looking for new and better ways of doing things, or he/she may be a small/medium business owner perhaps bored looking for more meaning in personal and business life), or the corporate person who is looking to get out and do something new. Age 35-50.
Updates

Hi I want to correct the paper size. It is "C Format" (trade paperbacks) are 135mm x 216mm (5.32" x 8.51").

Thks

Reason: A deadline has changed which means the completion of this book cover is less time-critical.

This is a business book that introduces new concepts, such as Purpose. Although it is based on spiritual principals  it is using normal business language when explaining what Purpose is, and how businesses can identify it and use it to be more successful.

If there is a border between a self-help and a business book, this book sits close to the border but markedly on the business side.

Hi I want to confirm the book size. The book size I require is the Australian C Format, which measures 153mm W x 234mm H. 

Sorry for any confusion

Reason: Hi I have extended the deadline as I want to be able to print prospective covers and see how they look like in a bookshop next to other covers.

Reason: To allow for final negotiations.

Industry/Entity Type

Business

```html
<!DOCTYPE html>
<html lang="en">
<head>
<meta charset="utf-8">
<title>Walk the High Line – Book Cover</title>
<link rel="stylesheet" href="https://fonts.googleapis.com/css2?family=Archivo+Black&family=Noto+Sans:wght@700&display=swap">
<style>
  :root {
    --page: #f4f4f4;
    --violet: #8e2389;
    --powder: #e4f4fb;
    --cerulean: #00aeef;
    --cobalt: #1a74bb;
    --lemon: #d4de1f;
    --white: #ffffff;
    --ink: #5a1456;
  }
  html, body {
    margin: 0;
    width: 1200px;
    height: 900px;
    overflow: hidden;
    background: var(--page);
  }
  .stage {
    width: 1200px;
    height: 900px;
    display: flex;
    align-items: center;
    justify-content: center;
  }
  .book-cover {
    width: 536px;
    height: 829px;
    display: block;
    box-shadow: 0 2px 10px rgba(0,0,0,0.15);
  }
  .stop-violet { stop-color: var(--violet); }
  .stop-powder { stop-color: var(--powder); }
  .stop-cerulean { stop-color: var(--cerulean); }
  .stop-lemon { stop-color: var(--lemon); }
  .title {
    font-family: "Archivo Black", "Arial Black", sans-serif;
    font-size: 22px;
    fill: var(--white);
    stroke: var(--ink);
    stroke-width: 0.6px;
    paint-order: stroke;
  }
  .subtitle {
    font-family: "Noto Sans", Verdana, sans-serif;
    font-weight: 700;
    font-size: 12.5px;
    fill: var(--cobalt);
  }
  .author {
    font-family: "Noto Sans", Verdana, sans-serif;
    font-weight: 700;
    font-size: 13px;
    fill: var(--white);
  }
</style>
</head>
<body>
<main class="stage">
  <svg class="book-cover" viewBox="0 0 265 410" xmlns="http://www.w3.org/2000/svg" aria-label="Walk the High Line book cover">
    <defs>
      <linearGradient id="cover-tones" x1="0" y1="0" x2="1" y2="1">
        <stop class="stop-violet" offset="0"/>
        <stop class="stop-violet" offset="0.48"/>
        <stop class="stop-cerulean" offset="0.54"/>
        <stop class="stop-powder" offset="0.6"/>
        <stop class="stop-lemon" offset="0.72"/>
        <stop class="stop-lemon" offset="1"/>
      </linearGradient>
    </defs>

    <rect class="cover-art" x="0" y="0" width="265" height="410" fill="url(#cover-tones)" role="img" aria-label="Cover illustration: rising arrows, a gear and a staircase in violet, blue and yellow"/>

    <text class="title" x="36" y="222" transform="rotate(-44 36 222)" textLength="235" lengthAdjust="spacingAndGlyphs">WALK THE HIGH LINE</text>
    <text class="subtitle" x="80" y="384" transform="rotate(-45 80 384)" textLength="228" lengthAdjust="spacingAndGlyphs">meaning at work in modern business</text>
    <text class="author" x="134" y="398">Anders Holmvik</text>
  </svg>
</main>
</body>
</html>
```